THE TALL COPPER ATLAS OF PORTS

subtitle: AN INTRO TO SEARCH ENGINE OPTIMIZATION
background: white
dimensions: 1562x2500

Target Market(s)

Marketing professionals

Industry/Entity Type

Digital Marketing

Font styles to use
Sans Serif

Colors
ffffff
1b1b1b
3176b5

Requirements
Should not have
• Images or graphics

```html
<!DOCTYPE html>
<html lang="en">
<head>
<meta charset="utf-8">
<title>The Tall Copper Atlas of Ports</title>
<link rel="stylesheet" href="https://fonts.googleapis.com/css2?family=Open+Sans:wght@500;600;700&display=swap">
<style>
  :root {
    --paper: #ffffff;
    --ink: #1b1b1b;
    --accent: #3176b5;
    --band: #777777;
    --edge: #7a7a7a;
  }
  html, body {
    margin: 0;
    padding: 0;
    overflow: hidden;
    background: var(--paper);
  }
  .cover {
    position: relative;
    width: 750px;
    height: 1200px;
    overflow: hidden;
    background: var(--band);
    font-family: "Open Sans", sans-serif;
  }
  .cover__page {
    position: absolute;
    left: 0;
    top: 0;
    width: 750px;
    height: 800px;
    box-sizing: border-box;
    background: var(--paper);
    border: 4px solid var(--edge);
    border-bottom: none;
  }
  .cover__volume {
    position: absolute;
    right: 30px;
    top: 22px;
    margin: 0;
    font-size: 40px;
    font-weight: 700;
    line-height: 1;
    color: var(--accent);
  }
  .cover__title {
    position: absolute;
    left: 58px;
    top: 298px;
    margin: 0;
    font-size: 98px;
    font-weight: 600;
    line-height: 91px;
    letter-spacing: -0.5px;
    color: var(--ink);
  }
  .cover__title span { display: block; }
  .cover__title .cover__keyword {
    font-weight: 700;
    color: var(--accent);
  }
  .cover__author {
    position: absolute;
    left: 57px;
    top: 1104px;
    margin: 0;
    font-size: 40px;
    font-weight: 500;
    line-height: 1;
    letter-spacing: 8px;
    color: var(--ink);
  }
</style>
</head>
<body>
  <main class="cover">
    <section class="cover__page">
      <p class="cover__volume">02</p>
      <h1 class="cover__title">
        <span>The</span>
        <span>Tall</span>
        <span>Copper</span>
        <span>Atlas of</span>
        <span class="cover__keyword">Ports</span>
      </h1>
    </section>
    <p class="cover__author">DANIEL PRESCOTT</p>
  </main>
</body>
</html>
```